Shop window posters and banners for a contact lens (Carlow&Birkett Velora Pro)

Please take a look at our appearance on Instagram (optique_valmire), where you can also see the shop windows. In this case we would like to advertise a specific contact lens in the shop window. For this we need a poster and a banner. I can send you pictures of the lens. The poster banner should be filled with questions such as: Are you already wearing High Quality? Does your lens also have a blue filter? Feel good even after wearing it for a long time? Make an appointment with our vision experts!

Target Market(s)

Reach people who are dissatisfied with their contact lenses at the end of the day. For whom it may be important to protect their eyes from blue light.

Requirements
Must have
• correspond to the style of the store

```html
<!DOCTYPE html>
<html lang="de">
<head>
<meta charset="utf-8">
<title>Optique Valmire – Velora Pro Poster</title>
<link rel="stylesheet" href="https://fonts.googleapis.com/css2?family=Barlow+Condensed:wght@300;400;500;600;700&display=swap">
<style>
  :root {
    --stage: #74a3b0;
    --navy: #22305e;
    --sky: #1a9ed4;
    --paper-top: #eef6f9;
    --paper-bottom: #cfe5ee;
    --white: #ffffff;
    --skin: #e8c2a6;
    --hair: #d9b98a;
  }
  html, body {
    margin: 0;
    padding: 0;
    width: 1067px;
    height: 1200px;
    overflow: hidden;
    background: var(--stage);
    font-family: "Barlow Condensed", "Arial Narrow", sans-serif;
  }
  .poster-frame {
    position: absolute;
    left: 117px;
    top: 40px;
    width: 833px;
    height: 1120px;
    overflow: hidden;
  }
  .poster {
    position: absolute;
    left: 0;
    top: 0;
    width: 922px;
    height: 1240px;
    transform: scale(0.9035);
    transform-origin: 0 0;
    background: radial-gradient(ellipse at 30% 35%, var(--paper-top) 0%, #ddeef4 55%, var(--paper-bottom) 100%);
    color: var(--navy);
  }
  .poster > * { position: absolute; margin: 0; line-height: 1; }

  .model-photo {
    left: 300px;
    top: 250px;
    width: 622px;
    height: 720px;
    background:
      radial-gradient(ellipse 38% 42% at 58% 42%, var(--skin) 0%, rgba(232,194,166,0.85) 55%, rgba(217,185,138,0) 100%),
      radial-gradient(ellipse 55% 60% at 60% 40%, rgba(217,185,138,0.9) 0%, rgba(217,185,138,0) 75%),
      radial-gradient(ellipse 70% 40% at 60% 100%, rgba(232,194,166,0.9) 0%, rgba(232,194,166,0) 80%);
  }

  .brand-name {
    left: 676px;
    top: 108px;
    width: 164px;
    text-align: center;
    font-size: 30px;
    font-weight: 600;
    line-height: 1.1;
    color: var(--navy);
  }

  .headline-intro { left: 58px; top: 82px; font-size: 64px; font-weight: 400; letter-spacing: 0.5px; }
  .headline-high { left: 56px; top: 141px; font-size: 132px; font-weight: 700; letter-spacing: -1px; }
  .headline-quality { left: 56px; top: 253px; font-size: 132px; font-weight: 700; letter-spacing: -1px; color: var(--sky); }

  .question { left: 59px; font-size: 52px; font-weight: 400; }
  .question.accent { color: var(--sky); font-weight: 500; }
  .q-lens { top: 413px; }
  .q-filter { top: 461px; }
  .q-feel-1 { top: 545px; }
  .q-feel-2 { top: 593px; }
  .q-feel-3 { top: 641px; }
  .divider { left: 58px; top: 520px; width: 157px; height: 5px; background: var(--navy); }

  .footer-wave { left: 0; top: 700px; width: 922px; height: 540px; }

  .cta { left: 0; width: 922px; text-align: center; font-size: 62px; font-weight: 500; color: var(--white); }
  .cta-1 { top: 910px; }
  .cta-2 { top: 977px; }
  .cta .accent { color: var(--sky); }

  .call-pill {
    left: 350px; top: 1078px; width: 222px; height: 37px;
    border-radius: 19px; background: var(--sky); color: var(--white);
    display: flex; align-items: center; justify-content: center; gap: 4px;
    font-size: 33px; font-weight: 400;
  }
  .call-pill svg { width: 26px; height: 26px; }
  .phone-number {
    left: 0; top: 1126px; width: 922px; text-align: center;
    font-size: 68px; font-weight: 600; color: var(--white);
  }

  .contact {
    top: 1108px; width: 240px;
    display: flex; flex-direction: column; align-items: center; gap: 10px;
    color: var(--white); font-size: 26px; font-weight: 400;
  }
  .contact-social { left: 17px; }
  .contact-web { left: 663px; }
  .contact .dot { width: 26px; height: 26px; border: 2.5px solid var(--white); border-radius: 50%; box-sizing: border-box; }
  .contact svg { width: 26px; height: 26px; }
</style>
</head>
<body>
  <div class="poster-frame">
    <div class="poster">
      <div class="model-photo" role="img" aria-label="Photo of a young woman with blonde hair putting in a contact lens with her fingertip"></div>

      <p class="brand-name">OPTIQUE<br>VALMIRE</p>

      <p class="headline-intro">TRAGEN SIE SCHON</p>
      <h1 class="headline-high">HIGH</h1>
      <p class="headline-quality">QUALITY?</p>

      <p class="question q-lens">HAT IHRE LINSE AUCH</p>
      <p class="question accent q-filter">BLAUFILTER?</p>
      <div class="divider"></div>
      <p class="question q-feel-1">GUTES GEFÜHL</p>
      <p class="question q-feel-2">AUCH NACH</p>
      <p class="question accent q-feel-3">LANGEM TRAGEN?</p>

      <svg class="footer-wave" viewBox="0 0 922 540" preserveAspectRatio="none">
        <path d="M0,225 Q461,43 922,225 L922,540 L0,540 Z" fill="var(--sky)"/>
        <path d="M0,238 Q461,52 922,238 L922,540 L0,540 Z" fill="var(--navy)"/>
      </svg>

      <p class="cta cta-1">MACHEN SIE EINEN <span class="accent">TERMIN</span></p>
      <p class="cta cta-2">MIT UNSEREN SEHEXPERTEN!</p>

      <div class="call-pill">
        <svg viewBox="0 0 24 24" aria-hidden="true">
          <path fill="#fff" d="M6.6 10.8a15.1 15.1 0 0 0 6.6 6.6l2.2-2.2c.3-.3.7-.4 1-.2 1.1.4 2.3.6 3.6.6.6 0 1 .4 1 1V20c0 .6-.4 1-1 1A17 17 0 0 1 3 4c0-.6.4-1 1-1h3.5c.6 0 1 .4 1 1 0 1.3.2 2.5.6 3.6.1.3 0 .7-.2 1L6.6 10.8z"/>
        </svg>
        <span>RUF UNS AN</span>
      </div>
      <p class="phone-number">00352/618905</p>

      <div class="contact contact-social">
        <span class="dot"></span>
        <span>optique_valmire</span>
      </div>
      <div class="contact contact-web">
        <svg viewBox="0 0 24 24" aria-hidden="true" fill="none" stroke="#fff" stroke-width="1.6">
          <circle cx="12" cy="12" r="10"/>
          <ellipse cx="12" cy="12" rx="4.5" ry="10"/>
          <path d="M2 12h20M4 7h16M4 17h16"/>
        </svg>
        <span>optiquevalmire.shop</span>
      </div>
    </div>
  </div>
</body>
</html>
```